Colourful Bold Design for Pet Insurance Website

PLEASE NOTE THAT THIS PROJECT HAS BEEN EXTENDED. Please read the PROJECT EXTENSION DOCUMENT BEFORE STARTING WORK ON ANY DESIGNS.

We are looking for a colourful bold new template design for our JOOMLA HOMEPAGE and a matching design for our new WORDPRESS BLOG.

The website will help pet owners work out which insurance policy best meets their needs. The aim of the website is to explain policy differences in a plain clear manner.

The website will need to have a professional colourful image. It needs to be BOLD, CLEAN AND SHARP rather than soft, pastel and cuddly.

COLOUR SCHEME
The website needs to have a bold colourful design on a white background.
On the inner pages we will have five different types of policies which will be colour coded. We would ideally therefore like to incorporate five distinct colours in the design. See attached document for example of colour schemes we like.

LOGO
We want to keep the existing logo. Please find the file attached. You may though change the logo colours.

CONTENT
One of the reasons for the new design is that we want to change the style of the homepage and include new content. Our current homepage can be found at www.furrow-cover-polls.co.uk.

Content Required
Slideshow
Article Intro.. About Pet Insurance
Policy Lookup Box (see existing site… you can change the design of this)
Six link options (see links on left of current page)
Latest Reviews (List of 6)
Ad (Same dimensions as currently on homepage)

News and Comment Section - To include Three or Four Articles, Title, Intro to article (probably 3 or 4 lines .. about 400px wide), Read more link
Social Media Section
Friendbook Plugin with Feed
Latest Tweets Plugin
Pet Charities Latest Tweets
Footer
Larger footer with lots of links grouped in sections

It does not need to include the clipart pic of the pets which is on the current homepage.

Examples of Websites and Templates We Like
http://www.pawlane.com/ (like colours… fonts…layout)
http://sitetheme.brightkiln.com/?template=upbeat&path=/... (like the clarity, "white" space etc)
http://www.layoutforge.com/demo/51872.html (like white space, clear easy to read fonts… don’t like colour scheme, size of top picture)
http://www.layoutforge.com/website-templates/63915.html (like colour scheme, use of white space)

FEEDBACK
I will provide lots of feedback on all designs submitted so that together we can get the best result.

For clarification this is a DESIGN ONLY project. Our website developer will view the designs before we make our final choice as he wants to ensure he can develop "sharp, practical and most importantly light weight web interface" from the design.

Just updated this brief to clarify design issues, content issues and to give some more examples of site designs I like. 

Please note that although we wish to keep the logo you can change the colours to suit your design. 

Please note that we have now added details of pictures we would be happy to use on the website.  We would prefer it if you used one of these.   Otherwise please ensure your picture includes a nice dog and nice cat and no people!

I have been delighted with the quality of the designs submitted for this project.  So much so that I am going to extend the project to include some additional inner pages.   The amended brief will be posted on here on Friday 10 May.   The deadline will be extended and the budget will also be increased. 

Reason: Additional inner pages now required. Budget will be increased. Revised brief to be posted on here Friday 10 May.

Target Market(s)

Pet owners in the UK who are confused about pet insurance. It therefore needs to be a bold design which is plain, clean and easy to read. It should use bold colours rather than pastels and should not use "cuddly" images.

Industry/Entity Type

Insurance

Requirements
Must have
• Bold clear and distinct colours (preferably 5)
Content as per uploaded file (not just content from existing site)
Easy to read fonts
Should not have
• Pastel colours
Cuddly images

```html
<!DOCTYPE html>
<html lang="en">
<head>
<meta charset="utf-8">
<title>Furrow Cover Polls UK</title>
<link rel="stylesheet" href="https://fonts.googleapis.com/css2?family=Roboto+Condensed:wght@400;700&family=Arimo:ital,wght@0,400;0,700;1,400&display=swap">
<style>
:root{
  --blue:#1a7ccc;
  --blue-dark:#1569b0;
  --blue-light:#6aaee8;
  --orange:#f47b20;
  --green:#6abf7b;
  --green-text:#3aa04a;
  --purple:#a550d6;
  --grey-bg:#e9eaeb;
  --text:#333;
  --line:#cfcfcf;
  --white:#fff;
}
*{margin:0;padding:0;box-sizing:border-box}
html,body{width:964px;height:1200px;overflow:hidden}
body{position:relative;background:var(--grey-bg);font-family:"Arimo",Arial,sans-serif;color:var(--text)}
.abs{position:absolute}
.cond{font-family:"Roboto Condensed",Arial,sans-serif}
.site-header{left:0;top:0;width:964px;height:118px;background:var(--blue)}
.brand{left:128px;top:28px;display:flex;align-items:center;gap:8px;color:var(--white);font-family:"Roboto Condensed",sans-serif;font-weight:700;font-size:22px;line-height:20px}
.brand-mark{width:44px;height:44px;border-radius:50%;background:var(--white);opacity:.9}
.social-top{right:134px;top:42px;display:flex;gap:9px}
.social-top span{width:22px;height:22px;border-radius:50%;background:#5aa6e6}
.page{left:126px;top:94px;width:712px;height:929px;background:var(--white)}
.main-nav{left:126px;top:94px;width:712px;height:36px;display:flex;border-bottom:1px solid var(--line);background:var(--white)}
.main-nav a{font-family:"Roboto Condensed",sans-serif;font-size:14px;color:#222;text-decoration:none;display:flex;align-items:center;justify-content:center;border-right:1px solid var(--line);height:36px;position:relative}
.main-nav a.active{color:var(--orange);border-bottom:3px solid var(--orange)}
.main-nav a.has-sub::after{content:"";position:absolute;bottom:5px;left:50%;width:5px;height:5px;border-right:1.5px solid #444;border-bottom:1.5px solid #444;transform:translateX(-50%) rotate(45deg)}
.slider{left:137px;top:153px;width:458px;height:224px;border:4px solid #e6e6e6;border-radius:6px;overflow:hidden;background:#f6f6f6}
.slider-photo{position:absolute;right:0;top:0;width:300px;height:216px;background:radial-gradient(ellipse at 60% 55%,#6b5b4e 0%,#a89886 35%,#f4f2ef 70%)}
.slider-text{position:absolute;left:12px;top:12px;color:var(--white)}
.slider-text h2{font-family:"Roboto Condensed",sans-serif;font-weight:700;font-size:28px;line-height:36px}
.slider-text p{font-family:"Roboto Condensed",sans-serif;font-size:16px;line-height:20px;margin-top:18px;width:160px}
.slider-nav{position:absolute;left:12px;top:170px;width:37px;height:20px;border-radius:10px;background:var(--orange)}
h1.welcome{left:139px;top:400px;font-family:"Roboto Condensed",sans-serif;font-size:20px;color:var(--blue);font-weight:400}
.intro{left:140px;top:432px;width:456px;font-size:10px;line-height:13px;color:#333}
.intro p+p{margin-top:13px}
.view-more{left:537px;top:531px;font-size:10px;color:var(--blue);font-weight:700}
.dots{border-top:1px dotted #aaa}
.popular{left:137px;top:563px;width:458px;height:206px;border:1px solid #dff0e2;border-radius:4px;background:#f5fbf6}
.popular h3{height:26px;background:var(--green);color:var(--white);font-family:"Roboto Condensed",sans-serif;font-size:16px;font-weight:400;line-height:26px;padding-left:10px;border-radius:3px}
.article{position:absolute;left:12px;width:436px}
.article .thumb{position:absolute;left:0;top:0;width:66px;height:48px;border:2px solid #fff;box-shadow:0 0 2px #aaa}
.article h4{position:absolute;left:80px;top:0;font-size:9px;color:var(--green-text);font-weight:700}
.article time{position:absolute;right:10px;top:0;font-size:9px;font-style:italic;color:var(--green-text)}
.article p{position:absolute;left:80px;top:12px;width:354px;font-size:9px;line-height:11.5px;text-align:justify;color:#444}
.article .more{position:absolute;right:4px;top:50px;font-size:9px;font-style:italic;color:var(--green-text);font-weight:700}
.quick-links{left:144px;top:797px;width:192px;list-style:none}
.quick-links li{height:27px;border-bottom:1px solid #bbb;font-size:12px;line-height:26px;padding-left:9px;position:relative;color:#333}
.quick-links li::before{content:"";position:absolute;left:0;top:11px;width:4px;height:4px;border-radius:50%;background:#555}
.reviews{left:370px;top:793px;width:225px}
.reviews h3{font-family:"Roboto Condensed",sans-serif;font-size:18px;font-weight:400;color:#333}
.review{margin-top:12px;position:relative}
.review+.review{margin-top:14px}
.review h4{font-size:9px;font-weight:700;padding-left:6px;position:relative}
.review h4::before{content:"";position:absolute;left:0;top:3px;width:3px;height:3px;border-radius:50%;background:#333}
.review .meta{font-size:8px;font-style:italic;color:#666;padding-left:6px}
.review p{font-size:9px;line-height:11.5px;margin-top:3px;padding-left:6px}
.review .rating{margin-top:3px;height:16px;background:#eee;display:flex;align-items:center;justify-content:space-between;padding:0 8px 0 2px;font-size:9px}
.review .stars{color:#f0a30a;font-size:13px;letter-spacing:-1px}
.policy-box{left:612px;top:153px;width:213px;height:144px;background:#f0f0f0;border:1px solid #e2e2e2}
.policy-box h3{height:29px;background:var(--purple);color:var(--white);font-family:"Roboto Condensed",sans-serif;font-size:18px;font-weight:400;line-height:29px;padding-left:44px;position:relative}
.policy-box h3 svg{position:absolute;left:11px;top:3px}
.select{position:absolute;left:16px;width:183px;height:25px;background:var(--white);border:1px solid #ccc;border-radius:3px;font-size:9px;color:#888;line-height:23px;padding-left:10px}
.select::after{content:"";position:absolute;right:6px;top:6px;width:11px;height:11px;border:1px solid #888;background:linear-gradient(#fff,#ddd)}
.ad{left:612px;top:313px;width:215px;height:179px;background:linear-gradient(#5bb04a,#3f8f30);overflow:hidden}
.ad-photo{position:absolute;left:-40px;top:-140px;width:295px;height:222px;border-radius:50%;background:linear-gradient(135deg,#e8c9a8,#b07a4a 55%,#7a5a3e)}
.ad-copy{position:absolute;left:0;top:86px;width:215px;text-align:center;color:var(--white)}
.ad-copy .org{font-family:"Roboto Condensed",sans-serif;font-size:11px;font-weight:700}
.ad-copy .line1{font-size:10px;margin-top:6px;letter-spacing:.5px}
.ad-copy .line2{font-size:10px;font-weight:700;letter-spacing:.5px}
.ad-copy .line3{font-size:6.5px;margin-top:4px}
.ad-copy .donate{display:inline-block;margin-top:6px;background:#5a2d82;font-size:7.5px;font-weight:700;padding:5px 12px}
.fb-box{left:612px;top:502px;width:214px;height:267px;border:1px solid #b8c3d8;background:var(--white);font-size:7px}
.fb-box .head{height:16px;background:#eef1f6;border-bottom:1px solid #b8c3d8;font-size:8px;font-weight:700;line-height:15px;padding-left:4px;color:#333}
.fb-post{position:absolute;left:8px;width:190px}
.fb-post .avatar{position:absolute;left:0;top:0;width:28px;height:28px;background:#999}
.fb-post .name{position:absolute;left:34px;top:2px;color:#3b5998;font-weight:700;font-size:8px}
.fb-post .body{position:absolute;left:34px;top:14px;width:150px;line-height:11px;color:#333}
.fb-faces{position:absolute;left:6px;top:170px;display:grid;grid-template-columns:repeat(6,30px);gap:3px}
.fb-faces span{height:30px;background:#8a8a8a}
.tw-box{left:612px;top:778px;width:215px;height:214px;background:var(--blue);border-radius:2px}
.tw-box .head{height:38px;color:var(--white);font-family:"Roboto Condensed",sans-serif;font-weight:700;font-size:11px;line-height:11px;padding:9px 0 0 36px;position:relative}
.tw-box .head::before{content:"";position:absolute;left:9px;top:7px;width:22px;height:22px;border-radius:50%;background:var(--white);opacity:.85}
.tw-list{position:absolute;left:4px;top:39px;width:207px;height:146px;background:var(--white);font-size:7.5px;line-height:10px;color:#333}
.tweet{position:absolute;left:6px;width:190px}
.tweet .avatar{position:absolute;left:0;top:0;width:22px;height:22px;background:#999}
.tweet .txt{position:absolute;left:30px;top:0;width:160px}
.tweet a{color:var(--blue);text-decoration:none}
.tweet .act{color:var(--blue);font-size:6.5px}
.tw-box .foot{position:absolute;left:0;bottom:0;width:100%;height:28px;color:var(--white);font-size:8px;display:flex;align-items:center;justify-content:space-between;padding:0 8px}
.tw-box .foot b{font-family:"Roboto Condensed",sans-serif;font-size:11px}
.site-footer{left:0;top:998px;width:964px;height:182px;background:var(--blue)}
.foot-brand{left:132px;top:1050px;display:flex;align-items:center;gap:10px;color:var(--white);font-family:"Roboto Condensed",sans-serif;font-weight:700;font-size:24px;line-height:22px}
.foot-brand .brand-mark{width:48px;height:48px}
.foot-col{top:1043px;color:var(--white)}
.foot-col h4{font-family:"Roboto Condensed",sans-serif;font-size:16px;font-weight:400;margin-bottom:6px}
.foot-col li{list-style:none;font-size:10px;line-height:15.8px}
.foot-div{top:1040px;width:0;height:120px;border-left:1px solid #3f93d8}
.follow li{display:flex;align-items:center;gap:10px;line-height:21.5px}
.follow li span{width:16px;height:16px;border-radius:2px}
.bottom-bar{left:0;top:1178px;width:964px;height:22px;background:var(--blue-light);color:var(--white);font-size:10px;line-height:22px}
</style>
</head>
<body>
<header class="abs site-header"></header>
<div class="abs brand"><span class="brand-mark"></span><span>Furrow Cover<br>Polls UK</span></div>
<div class="abs social-top" aria-label="Social links"><span></span><span></span><span></span><span></span></div>

<div class="abs page"></div>
<nav class="abs main-nav">
  <a class="active" style="width:83px">HOME</a>
  <a class="has-sub" style="width:98px">POLICIES</a>
  <a style="width:111px">GLOSSARY</a>
  <a style="width:125px">FACT SHEETS</a>
  <a style="width:143px">SURVEY REPORTS</a>
  <a style="width:152px;border-right:0">NEWS &amp; COMMENT</a>
</nav>

<section class="abs slider">
  <div class="slider-photo" role="img" aria-label="Photo of a spaniel lying beside a tabby cat on white"></div>
  <svg class="abs" style="left:0;top:0" width="450" height="216"><polygon points="0,0 270,0 135,216 0,216" fill="#1a7ccc"/><line x1="12" y1="88" x2="200" y2="88" stroke="#4d9bdb" stroke-width="1"/></svg>
  <div class="slider-text">
    <h2>We do not sell pet<br>Insurance...</h2>
    <p>or receive commission from pet insurance companies...</p>
  </div>
  <div class="slider-nav"><svg width="37" height="20"><path d="M14 6 L10 10 L14 14 M23 6 L27 10 L23 14" stroke="#fff" stroke-width="2" fill="none"/></svg></div>
</section>

<h1 class="abs welcome">Welcome to Furrow Cover Polls UK</h1>
<div class="abs intro">
  <p>This is an independent website dedicated to helping you to find the best pet insurance policy for your pet Here you will find unbiased detailed information about almost all of the 205 pet insurance policies currently available in the UK (we hope the other 3 will follow shortly!)</p>
  <p>We do NOT sell any pet insurance policies nor do we receive commission from any insurance companies simply dummy text of the printing and typesetting industry. Lorem Ipsum has been the industry's standard dummy text ever since the 1500s,</p>
</div>
<div class="abs view-more">View more ›</div>
<div class="abs dots" style="left:140px;top:548px;width:454px"></div>

<section class="abs popular">
  <h3>Popular Articles</h3>
  <div class="article" style="top:44px">
    <div class="thumb" role="img" aria-label="Photo of a dog looking out of a car window" style="background:linear-gradient(#3a6fb5,#8fb0d8 60%,#5a8a3a)"></div>
    <h4>Lorem Ipsum is simply dummy text</h4><time>09/05/2013</time>
    <p>simply dummy text of the printing and typesetting industry. Lorem Ipsum has been the industry's standard of the printing and typesetting industry. Lorem Ipsum has been the industry's standard dummy text ever since the 1500s,</p>
    <span class="more">read more ›</span>
  </div>
  <div class="dots" style="position:absolute;left:12px;top:113px;width:432px"></div>
  <div class="article" style="top:127px">
    <div class="thumb" role="img" aria-label="Photo of two lion cubs" style="background:linear-gradient(135deg,#c9a878,#8a6a44)"></div>
    <h4>Lorem Ipsum is simply dummy text</h4><time>09/05/2013</time>
    <p>simply dummy text of the printing and typesetting industry. Lorem Ipsum has been the industry's standard of the printing and typesetting industry. Lorem Ipsum has been the industry's standard dummy text ever since the 1500s,</p>
    <span class="more">read more ›</span>
  </div>
</section>

<ul class="abs quick-links">
  <li>Policy Files</li><li>Policy Search</li><li>Fact Sheets</li><li>Policy Listings by Type</li><li>Claims Survey</li><li>2013 Price Survey Report</li>
</ul>
<div class="abs dots" style="left:362px;top:795px;width:0;height:200px;border-top:0;border-left:1px dotted #aaa"></div>
<section class="abs reviews">
  <h3>Latest Reviews</h3>
  <div class="review">
    <h4>Simply dummy text simply dummy.</h4>
    <div class="meta">By Miles Orrin, 9 May 2013, 09:19 hrs IST</div>
    <p>simply dummy text of the printing and typesetting industry pesetting industry Ipsum has industry's</p>
    <div class="rating"><span class="stars">★★★☆☆</span><span>View more..</span></div>
  </div>
  <div class="review">
    <h4>Simply dummy text simply dummy.</h4>
    <div class="meta">By Miles Orrin, 9 May 2013, 09:19 hrs IST</div>
    <p>simply dummy text of the printing and typesetting industry pesetting industry Ipsum has industry's</p>
    <div class="rating"><span class="stars">★★★☆☆</span><span>View more..</span></div>
  </div>
</section>

<aside class="abs policy-box">
  <h3><svg width="28" height="28"><circle cx="12" cy="12" r="9" fill="#dfefff" stroke="#fff" stroke-width="2"/><line x1="19" y1="19" x2="26" y2="26" stroke="#555" stroke-width="3"/></svg>Check Out a Policy</h3>
  <div class="select" style="top:81px">Select Company</div>
  <div class="select" style="top:122px">Select Policy</div>
</aside>

<aside class="abs ad">
  <div class="ad-photo" role="img" aria-label="Photo of a woman hugging a rescue puppy"></div>
  <div class="ad-copy">
    <div class="org">Pawhaven Trust</div>
    <div class="line1">IT'S THE GIFT THAT</div>
    <div class="line2">KEEPS ON GIVING.</div>
    <div class="line3">Help homeless pets and donate this holiday season.</div>
    <div class="donate">Donate Now</div>
  </div>
</aside>

<aside class="abs fb-box">
  <div class="head">Find us on Friendbook</div>
  <div class="fb-post" style="top:24px"><div class="avatar" role="img" aria-label="Profile picture"></div><div class="name">Dana Whitfield</div><div class="body">▢ Like &nbsp;You like this.</div></div>
  <div class="dots" style="position:absolute;left:4px;top:60px;width:200px;border-top:1px solid #ddd"></div>
  <div class="fb-post" style="top:68px"><div class="avatar" role="img" aria-label="Profile picture"></div><div class="name">Dana Whitfield</div><div class="body">I think all of Mexico should throw a party for my birthday this year. Does May 5th work for you?<br><span style="color:#888">18 hours ago</span></div></div>
  <div style="position:absolute;left:6px;top:156px">You and 14,596 others like <span style="color:#3b5998">Dana Whitfield.</span></div>
  <div class="fb-faces" role="img" aria-label="Grid of fan profile pictures"><span></span><span></span><span></span><span></span><span></span><span></span><span></span><span></span><span></span><span></span></div>
  <div style="position:absolute;left:6px;top:244px;font-size:6px;color:#666">Friendbook social plugin</div>
</aside>

<aside class="abs tw-box">
  <div class="head">Furrow Cover<br>Polls UK</div>
  <div class="tw-list">
    <div class="tweet" style="top:6px"><div class="avatar" role="img" aria-label="Profile picture"></div><div class="txt"><a>quiet_harlow</a> RT <a>@buildnook</a>: "Optimize it" package released on our: <a>http://shrt.lk/itdq3Y</a> and associated blog post here: <a>http://shrt.lk/mxDdc3</a> <a>#cmsbox #cg11</a><br><span class="act">2 minutes ago · reply · retweet · favorite</span></div></div>
    <div style="position:absolute;left:0;top:90px;width:207px;text-align:center;font-size:6.5px;border-top:1px solid #eee">more than 1 new tweet</div>
    <div class="tweet" style="top:108px"><div class="avatar" role="img" aria-label="Profile picture"></div><div class="txt"><a>Brennick</a> Wondering why there is no really good blog package for Cmsbox... have I missed something? <a>#cmsbox #blog</a><br><span class="act">7 minutes ago · reply · retweet · favorite</span></div></div>
  </div>
  <div class="foot"><b>Chirper</b><span>Join the conversation</span></div>
</aside>

<footer class="abs site-footer"></footer>
<div class="abs foot-brand"><span class="brand-mark"></span><span>Furrow Cover<br>Polls UK</span></div>
<div class="abs foot-div" style="left:363px"></div>
<div class="abs foot-div" style="left:500px"></div>
<div class="abs foot-div" style="left:628px"></div>
<div class="abs foot-col" style="left:400px"><h4>Site Map</h4><ul><li>Find a Vet</li><li>Learn</li><li>Care</li><li>Train</li><li>Shop</li><li>Sitemap</li></ul></div>
<div class="abs foot-col" style="left:529px"><h4>Links</h4><ul><li>About Us</li><li>Privacy Policy</li><li>Terms of Use</li><li>Contact Us</li><li>Media Kit</li></ul></div>
<div class="abs foot-col follow" style="left:665px"><h4>Follow Us</h4><ul>
  <li><span style="background:#f26522"></span>Follow us RSS</li>
  <li><span style="background:#3b5998"></span>Follow us Friendbook</li>
  <li><span style="background:#d34836"></span>Follow us Circlesy</li>
  <li><span style="background:#33aaf0"></span>Follow us Chirper</li>
</ul></div>
<div class="abs bottom-bar"><span style="position:absolute;left:131px">Privacy Policy &nbsp;&nbsp;| &nbsp;&nbsp;Legal &nbsp;&nbsp;| &nbsp;&nbsp;About Furrow Cover Polls UK</span><span style="position:absolute;right:126px">Copyright © 2013 Furrow Cover Policy Polls</span></div>
</body>
</html>
```